Business cards for a tribute and obituary website

Our website is called Tribute Lantern.

It is a special place online for people to remember their loved ones who have passed away, through obituaries and tributes. Friends and family can also convey their condolences on the deceased's memorial page. Celebrating the life of the deceased and remembering their legacy is very important to us – death should not be just about grieving.

We would like the card to look tasteful and modern. The design should ideally not have colours that are too bright. The logo and website URL, www.tributelantern.example should be visible on the front of the card, with our slogan "Celebrating a life passed" on the back.

The design should communicate our purpose – remembering loved ones who have passed – and also a lighter tone of celebrating life. It should not look like a funeral director's card!

Our logo has been attached. Looking forward to some beautiful designs! Get creative :)
Updates

Project Deadline Extended
Reason: Thank you all for your designs. The rest of my team and I have not reached a decision on which design to select and I am collecting feedback from them. I will provide feedback for any changes that need to be made soon. It would be great if we could see more original designs and in more colours! We will definitely select a design by this deadline.

Industry/Entity Type

Business

Contact Information for Business Card

Wendy Lumb
Project Manager
614772390
wendylumb@tributelantern.example

Font styles to use
Serif
Sans Serif

Requirements
Must have
• Logo and website address (www.tributelantern.example) on the front.
Nice to have
• Hi designers! It would be nice to see alternative colours – feel free to try out colours that are tasteful and subtle. The colour of the business card does not have to be the same as the logo.
• We would also like to see the logo used in different ways, perhaps a glossy or embossed finish. The card should look stylish.

```html
<!DOCTYPE html>
<html lang="en">
<head>
<meta charset="utf-8">
<title>Tribute Lantern – Business Cards</title>
<link rel="stylesheet" href="https://fonts.googleapis.com/css2?family=Lato:wght@300;400;700&display=swap">
<style>
  :root {
    --backdrop: #dcdcdc;
    --card-navy: #0a2b4a;
    --accent-blue: #3aa3de;
    --accent-light: #5cbcef;
    --accent-deep: #1d7fbf;
  }
  * { box-sizing: border-box; margin: 0; padding: 0; }
  html, body {
    width: 1200px;
    height: 926px;
    overflow: hidden;
    background: var(--backdrop);
    font-family: "Lato", sans-serif;
  }
  .canvas {
    position: relative;
    width: 1200px;
    height: 926px;
  }
  .card {
    position: absolute;
    width: 640px;
    height: 366px;
    background: var(--card-navy);
    overflow: hidden;
    box-shadow: 0 6px 18px rgba(0,0,0,0.18);
  }
  .card-front { left: 470px; top: 70px; }
  .card-back  { left: 90px;  top: 490px; }

  .brand {
    display: flex;
    align-items: center;
    color: var(--accent-blue);
    font-weight: 700;
    line-height: 0.95;
  }
  .brand-dot {
    flex: none;
    border-radius: 50%;
    background: var(--accent-blue);
  }
  .brand-name span { display: block; }

  .card-front .brand {
    position: absolute;
    left: 150px;
    top: 100px;
    font-size: 50px;
    gap: 18px;
  }
  .card-front .brand-dot { width: 60px; height: 60px; }

  .website {
    position: absolute;
    left: 228px;
    top: 224px;
    color: var(--accent-blue);
    font-size: 17px;
    font-weight: 400;
    letter-spacing: 0.8px;
  }

  .card-back .brand {
    position: absolute;
    left: 40px;
    top: 44px;
    font-size: 30px;
    gap: 12px;
  }
  .card-back .brand-dot { width: 38px; height: 38px; }

  .contact {
    position: absolute;
    left: 44px;
    top: 150px;
    color: var(--accent-blue);
  }
  .contact-name {
    font-size: 27px;
    font-weight: 400;
    letter-spacing: 1.5px;
    text-transform: uppercase;
    line-height: 1;
  }
  .contact-role {
    font-size: 12px;
    font-weight: 400;
    letter-spacing: 1px;
    text-transform: uppercase;
    margin-top: 3px;
  }
  .contact-lines {
    margin-top: 22px;
    font-size: 15px;
    font-weight: 300;
    line-height: 1.45;
    letter-spacing: 0.3px;
  }
  .slogan {
    margin-top: 18px;
    font-size: 14px;
    font-weight: 400;
    letter-spacing: 0.5px;
    color: var(--accent-light);
  }

  .emblem-field {
    position: absolute;
    right: 0;
    top: 96px;
    width: 290px;
    height: 270px;
    background: linear-gradient(135deg, var(--accent-light) 0%, var(--accent-blue) 55%, var(--accent-deep) 100%);
    opacity: 0.85;
  }

  .base-band {
    position: absolute;
    left: 0;
    bottom: 0;
    width: 100%;
    height: 30px;
  }
</style>
</head>
<body>
<main class="canvas">

  <section class="card card-front" aria-label="Card front">
    <div class="brand">
      <span class="brand-dot"></span>
      <span class="brand-name"><span>Tribute</span><span>Lantern</span></span>
    </div>
    <p class="website">www.tributelantern.example</p>
  </section>

  <section class="card card-back" aria-label="Card back">
    <div class="brand">
      <span class="brand-dot"></span>
      <span class="brand-name"><span>Tribute</span><span>Lantern</span></span>
    </div>

    <div class="contact">
      <p class="contact-name">Wendy Lumb</p>
      <p class="contact-role">Project Manager</p>
      <div class="contact-lines">
        <p>614772390</p>
        <p>wendylumb@tributelantern.example</p>
      </div>
      <p class="slogan">Celebrating a life passed</p>
    </div>

    <svg class="base-band" viewBox="0 0 640 30" preserveAspectRatio="none" aria-hidden="true">
      <rect x="0" y="6" width="640" height="24" fill="var(--accent-blue)"/>
      <rect x="0" y="6" width="640" height="4" fill="var(--accent-light)"/>
    </svg>

    <div class="emblem-field" role="img" aria-label="Large cropped brand emblem in light blue"></div>
  </section>

</main>
</body>
</html>
```